Marlow Poise & Image Consultancy

Hi, I need a brochure design for my personal styling business. I have downloaded the company logo along with the content of the services offered for the brochure. Being a colour and styling business I would been keen on having some pictures of timeless fashion or colour samples, This is not absolutely necessary just an idea. I had also thought about changing and naming the services offered with a feminine, fun interesting type of theme. This may make it more inviting, I would be really interested in any of your creative ideas in this area. I will be deciding on the business card design in the next couple of days. I will download the design for this once I have made the decision. I will be okay to pay for any photo images that may be required if the brochure is selected. I had envisaged a tri fold brochure standard letter size with two folds (8.5" by 11inchs) however I am open to any suggestions. Please feel free to make any changes or modification's to the content, font etc in the files downloaded for the brochure. Many Thanks.
Updates
Project Deadline Extended
Reason: I need to extend the time for this project as I do not have all of content required for the brochure confirmed. Many Thanks
Industry/Entity Type
Fashion
Font styles to use
Look and feel
Each slider illustrates characteristics of the customer's brand and the style your logo design should communicate.

```html
<!DOCTYPE html>
<html lang="en">
<head>
<meta charset="utf-8">
<title>Premium Styling Packages – Tri-fold Brochure</title>
<link rel="stylesheet" href="https://fonts.googleapis.com/css2?family=Comfortaa:wght@700&family=Berkshire+Swash&family=Open+Sans:wght@400;600&display=swap">
<style>
:root{
  --bg:#e9e6e1;
  --paper:#ffffff;
  --gold:#f4b41a;
  --ink:#1b1b1b;
  --bar:#3b3b3b;
  --text:#333333;
  --muted:#6b6b6b;
  --grey-photo-a:#9a9a9a;
  --grey-photo-b:#5f5f5f;
}
*{box-sizing:border-box;margin:0;padding:0}
html,body{width:1200px;height:960px;overflow:hidden;background:var(--bg)}
body{font-family:"Open Sans",Arial,sans-serif;color:var(--text)}
.brochure{position:absolute;left:40px;top:47px;width:1120px;height:866px;display:flex;background:var(--paper);box-shadow:0 8px 24px rgba(0,0,0,.18)}
.panel{position:relative;width:373.33px;height:100%;overflow:hidden}
.panel + .panel{border-left:1px solid #ddd}
.photo{position:absolute}
.heading-band{position:absolute;left:0;right:0;height:46px;background:var(--ink);display:flex;align-items:center;justify-content:center;border-bottom:4px solid var(--gold)}
.heading-band h2{font-family:"Comfortaa",Arial,sans-serif;font-weight:700;font-size:23px;color:var(--gold);letter-spacing:.3px;white-space:nowrap}
.sub-band{position:absolute;left:0;right:0;height:28px;background:var(--gold);display:flex;align-items:center;padding-left:14px}
.sub-band h3{font-family:"Berkshire Swash",Georgia,serif;font-weight:400;font-size:15px;color:var(--ink);white-space:nowrap}
.copy{position:absolute;left:20px;right:20px;font-size:12.5px;line-height:1.45;color:var(--text)}
.package-list{position:absolute;left:20px;right:10px;list-style:none}
.package-list li{display:flex;align-items:center;height:21px;margin-bottom:6px}
.package-list .num{flex:none;width:22px;height:21px;background:var(--gold);color:var(--ink);font-weight:600;font-size:12px;display:flex;align-items:center;justify-content:center}
.package-list .label{height:21px;display:flex;align-items:center;padding:0 22px 0 8px;font-size:11px;white-space:nowrap;background:var(--bar);color:#eee;clip-path:polygon(0 0,100% 0,calc(100% - 10px) 100%,0 100%);border-radius:0 8px 0 0}
.package-list.light .label{background:#f2f2f2;color:var(--ink)}
.price{position:absolute;left:20px;font-size:10.5px;color:var(--muted);white-space:nowrap}
.on-photo .copy,.on-photo .price{color:#f4f4f4}
.service-list{position:absolute;left:20px;right:20px;list-style:none;font-size:12.5px;line-height:1.45}
.service-list li{position:relative;padding-left:20px;margin-bottom:8px}
.service-list li::before{content:"";position:absolute;left:0;top:5px;width:9px;height:9px;background:var(--gold)}
</style>
</head>
<body>
<main class="brochure">

  <section class="panel panel-left">
    <div class="photo" style="left:0;top:0;width:186px;height:90px;background:linear-gradient(135deg,#d9b08c,#8c6a4f)" role="img" aria-label="Smiling woman in a sun hat"></div>
    <div class="photo" style="left:187px;top:0;width:186px;height:90px;background:linear-gradient(135deg,#e8d6c9,#b07a8a)" role="img" aria-label="Young woman in a headscarf laughing"></div>
    <div class="photo" style="left:0;top:91px;width:124px;height:84px;background:linear-gradient(135deg,#cfcfcf,#7a7a7a)" role="img" aria-label="Black and white photo of friends shopping"></div>
    <div class="photo" style="left:125px;top:91px;width:124px;height:84px;background:linear-gradient(135deg,#c9c2bb,#8a847d)" role="img" aria-label="Women walking with shopping bags"></div>
    <div class="photo" style="left:250px;top:91px;width:123px;height:84px;background:linear-gradient(135deg,#c0607d,#3b4f8a)" role="img" aria-label="Friends in colourful outfits"></div>

    <div class="heading-band" style="top:185px"><h2>Premium Styling Packages</h2></div>
    <div class="sub-band" style="top:238px"><h3>Special Occasion Style Me Beautiful Package</h3></div>
    <p class="copy" style="top:276px">This is a great experience for weddings, birthdays, or just wanting to look your absolute best for any occasion. Treat someone special to the ultimate gift. Gift vouchers &amp; before and after photos avail able on request.</p>

    <ol class="package-list" style="top:370px">
      <li><span class="num">1</span><span class="label" style="min-width:170px">Consultation</span></li>
      <li><span class="num">2</span><span class="label" style="min-width:178px">Personal shopping service</span></li>
      <li><span class="num">3</span><span class="label" style="min-width:186px">Hair (accompaniment to hair salon)</span></li>
      <li><span class="num">4</span><span class="label" style="min-width:194px">Make up /Make over</span></li>
    </ol>
    <p class="price" style="top:484px">Price $ 185.00 (This does not include cost of hair salon)</p>

    <div class="sub-band" style="top:512px"><h3>The Forever Gorgeous Package</h3></div>
    <p class="copy" style="top:550px">Discover and Shine with a new signature style.This package will empower you with the confidence to dress for success every day.</p>
  </section>

  <section class="panel panel-middle on-photo">
    <div class="photo" style="left:0;top:0;width:100%;height:480px;background:linear-gradient(160deg,var(--grey-photo-a),var(--grey-photo-b))" role="img" aria-label="Greyscale portrait of a woman used as background"></div>

    <ol class="package-list light" style="top:22px">
      <li><span class="num">1</span><span class="label" style="min-width:200px">Style &amp; Colour Consultation</span></li>
      <li><span class="num">2</span><span class="label" style="min-width:210px">Personal Shopping Service</span></li>
      <li><span class="num">3</span><span class="label" style="min-width:220px">Make up Lesson</span></li>
      <li><span class="num">4</span><span class="label" style="min-width:230px">Style me complete consultation (accessories &amp; shoes)</span></li>
      <li><span class="num">5</span><span class="label" style="min-width:240px">Hair (accompaniment to hair salon)</span></li>
    </ol>
    <p class="price" style="top:162px">Price $340.00 (This does not include the cost of hair salon)</p>

    <div class="sub-band" style="top:190px"><h3>The Forever Gorgeous Package</h3></div>
    <p class="copy" style="top:228px">Discover and Shine with a new signature style.This package will empower you with the confidence to dress for success every day.</p>

    <ol class="package-list light" style="top:300px">
      <li><span class="num">1</span><span class="label" style="min-width:200px">Wardrobe clear out&amp;reassess</span></li>
      <li><span class="num">2</span><span class="label" style="min-width:210px">Style &amp; colour consultation</span></li>
      <li><span class="num">3</span><span class="label" style="min-width:230px">Style me complete consultation (accessories &amp; shoes)</span></li>
    </ol>
    <p class="price" style="top:386px">Price $265.00</p>

    <div class="photo" style="left:0;top:480px;width:100%;height:200px;background:linear-gradient(135deg,#b69a6e,#5e4a33)" role="img" aria-label="Woman in a hat laughing against a stone wall"></div>
    <div class="photo" style="left:0;top:681px;width:200px;height:185px;background:linear-gradient(135deg,#3f86a8,#d78a4c)" role="img" aria-label="Friends smiling together outdoors"></div>
    <div class="photo" style="left:201px;top:681px;width:173px;height:185px;background:linear-gradient(135deg,#f1d7b5,#c99a6a)" role="img" aria-label="Blonde woman in sunglasses"></div>
  </section>

  <section class="panel panel-right">
    <div class="heading-band" style="top:28px"><h2>Premium Styling Packages</h2></div>
    <p class="copy" style="top:88px">Time for a change? Take a fresh look and discover how to dress in a style that reflects your personal lifestyle. Be confident, look amazing &amp; feel great about the way that you look every day. Some people always look effortlessly stylish, looking good is all about knowing what suits you.</p>

    <div class="photo" style="left:0;top:210px;width:200px;height:230px;background:linear-gradient(135deg,#8fc6d6,#c9545f)" role="img" aria-label="Colourful clothes hanging on a rail"></div>
    <div class="photo" style="left:201px;top:190px;width:172px;height:250px;background:linear-gradient(135deg,#e3b7a0,#b0352a)" role="img" aria-label="Red-haired woman posing"></div>
    <div class="photo" style="left:110px;top:330px;width:110px;height:110px;background:linear-gradient(135deg,#d8a8a0,#4a2f35)" role="img" aria-label="Woman browsing a clothing store"></div>

    <div class="sub-band" style="top:458px"><h3>Personal Styling Services</h3></div>
    <ul class="service-list" style="top:500px">
      <li>Colour Analysis: you will discover your colours and how to wear them with confidence.</li>
      <li>Image &amp;Style Consultation - Express your image &amp; personality through the clothes that you wear and how you wear them. Learn how to select fabrics and clothing styles that will suit &amp; flatter your shape, and how to coordinate them.</li>
    </ul>
  </section>

</main>
</body>
</html>
```